Quarterly real estate newsletter

I need to update the layout of my newsletter so that the address can be printed on the newsletter itself. I also need to update the overall design. I need a template that I can use to edit the content going forward. This will be mailed to owners of homes worth $2,000,000 or more, so needs to be very polished and professional looking.
Below is the printer template that I need to use. Also is the last newsletter I sent, in Publisher format. The Cypress Report is a partial conversion to the new template, but still needs a lot of work. That is not how I want the final version to look.
On the cover, instead of a graph at the bottom, I would like a graphic with a few key market statistics (e.g. Median price, homes sold, average days on market) with some nice graphical elements, large arrows point up or down.
Inside I would like:
- an article with photos
- A list of recent solds
- our photo quiz
- a chart (like the one currently on the front)
- a second article (if there is room)
- contact info
The back is okay, although I think it could look a little cleaner
San Francisco home owners
Real Estate

```html
<!DOCTYPE html>
<html lang="en">
<head>
<meta charset="utf-8">
<title>The Cypress Report Update — Issue No. 05</title>
<link href="https://fonts.googleapis.com/css2?family=Open+Sans:wght@400;600&family=Oswald:wght@300;600&family=Source+Sans+3:wght@400;600;700&display=swap" rel="stylesheet">
<style>
  :root{
    --navy:#1c2b57;
    --slate:#474a50;
    --ink:#222;
    --orange:#f7913d;
    --green:#0f6b45;
    --paper:#fff;
  }
  *{box-sizing:border-box;margin:0;padding:0}
  html,body{width:1200px;height:934px;overflow:hidden;background:var(--paper)}
  body{position:relative;font-family:"Open Sans",sans-serif;color:var(--ink)}
  .abs{position:absolute}

  /* postage indicia */
  .indicia{left:38px;top:42px;width:107px;height:93px;border:1px solid #333;}
  .indicia-text{position:absolute;left:50%;top:50%;transform:translate(-50%,-50%) rotate(-90deg);
    font-family:Arial,sans-serif;font-size:13px;line-height:16px;white-space:nowrap;text-align:left}
  .indicia-text b{font-weight:700}

  /* agent card */
  .agent-card{left:26px;top:400px;width:561px;height:210px;background:var(--slate)}
  .agent-band{position:absolute;left:0;top:22px;width:300px;height:100px;background:var(--navy);color:#fff;text-align:center;padding-top:14px}
  .agent-band::after{content:"";position:absolute;right:-20px;top:0;border-top:50px solid transparent;border-bottom:50px solid transparent;border-left:20px solid var(--navy)}
  .agent-band h2{font-family:"Source Sans 3",sans-serif;font-weight:700;font-size:23px;line-height:26px;letter-spacing:-.3px}
  .agent-band .name{font-family:"Source Sans 3",sans-serif;font-weight:600;font-size:20px;line-height:24px}
  .agent-band .role{font-family:"Source Sans 3",sans-serif;font-size:14px;line-height:20px}
  .contacts{position:absolute;left:18px;top:131px;color:#fff;font-family:"Source Sans 3",sans-serif;font-size:14px;list-style:none}
  .contacts li{height:24px;display:flex;align-items:center;gap:10px}
  .contacts svg{width:16px;height:16px}
  .sales-map{position:absolute;left:312px;top:9px;width:240px;height:193px;background:linear-gradient(135deg,#f3e6ea,#e9d0d8 55%,#d9eadc)}

  .intro{left:26px;top:630px;width:561px;font-size:9.6px;line-height:17.8px;text-align:justify}

  .bullets{top:786px;list-style:none;font-size:9.6px}
  .bullets li{height:20.8px;display:flex;align-items:center;gap:7px}
  .bullets svg{width:10px;height:10px;flex:none}

  /* cover */
  .issue{left:613px;top:26px;width:163px;height:90px;z-index:2;color:#fff;text-align:center;font-family:"Source Sans 3",sans-serif;font-size:14px;line-height:17px;padding-top:21px}
  .panel-bg{position:absolute;left:0;top:0;width:100%;height:100%;z-index:-1}
  .masthead{left:790px;top:16px}
  .masthead h1{font-family:"Oswald",sans-serif;font-weight:600;font-size:38px;line-height:48px;letter-spacing:-.3px;color:#111}
  .masthead p{font-family:"Oswald",sans-serif;font-weight:300;font-size:26px;line-height:28px;color:#111;letter-spacing:-.6px}
  .hero{left:613px;top:98px;width:561px;height:250px;z-index:1;background:linear-gradient(180deg,#4c8fd6 0%,#a9cdef 45%,#c98a57 62%,#4f6b33 80%,#6b5a3c 100%)}

  .sidebar{left:613px;top:348px;width:163px;height:349px;z-index:1;color:#fff;text-align:center}
  .portrait{position:absolute;left:23px;top:19px;width:118px;height:149px;border:4px solid #fff;background:linear-gradient(180deg,#8a9a43,#c9a27e 60%,#9cc1dd)}
  .sidebar .name{position:absolute;top:181px;width:100%;font-family:"Source Sans 3",sans-serif;font-size:16px}
  .sidebar .role{position:absolute;top:202px;width:100%;font-family:"Source Sans 3",sans-serif;font-size:11px}
  .brokerage{position:absolute;top:238px;width:100%;font-family:"Source Sans 3",sans-serif}
  .brokerage .mark{font-size:22px;font-weight:600;line-height:26px}
  .brokerage .sub{font-size:9.5px;letter-spacing:.3px;font-weight:600;line-height:14px}

  .article{left:791px;top:362px;width:373px}
  .article h2{font-family:"Source Sans 3",sans-serif;font-weight:700;font-size:21px;line-height:30px;color:#111}
  .article .dek{font-family:"Source Sans 3",sans-serif;font-size:13px;line-height:22px;margin-bottom:3px}
  .article .body{font-size:9.1px;line-height:18.1px;text-align:justify}

  .chart{left:710px;top:712px;width:420px;height:198px}
  .chart-label{position:absolute;font-family:"Source Sans 3",sans-serif;font-weight:600;font-size:11.5px}
</style>
</head>
<body>

<div class="abs indicia">
  <div class="indicia-text">Presorted<br>Standard<br>US Postage<br><b>PAID</b><br>Berkeley, CA<br>Permit #4702</div>
</div>

<section class="abs agent-card">
  <div class="agent-band">
    <h2>DANIEL’S RECENT SALES</h2>
    <div class="name">Daniel Hale</div>
    <div class="role">Luxury Property Specialist</div>
  </div>
  <ul class="contacts">
    <li><svg viewBox="0 0 16 16" fill="none" stroke="#fff" stroke-width="1.3"><path d="M2 7c0-3 12-3 12 0l-2 1.5-2-1V6H6v1.5l-2 1z"/><rect x="4" y="9" width="8" height="4" rx="1"/></svg>Contact Us: 415.555.0142</li>
    <li><svg viewBox="0 0 16 16" fill="#fff"><path d="M15 1 1 7l5 2 1 6 2-4 4 3z"/></svg>Mail Id: dan@hale-sf.com</li>
    <li><svg viewBox="0 0 16 16" fill="none" stroke="#fff" stroke-width="1.2"><circle cx="8" cy="8" r="6.5"/><ellipse cx="8" cy="8" rx="3" ry="6.5"/><path d="M1.5 8h13M2.5 5h11M2.5 11h11"/></svg>Website Address: www.hale-sf.com</li>
  </ul>
  <div class="sales-map" role="img" aria-label="Street map of District 7 with recent sale locations marked"></div>
</section>

<p class="abs intro">There are Many Variations of Passages of Lorem Ipsum Available but the Majority have Suffered Alteration in some form by Injected Humour or Randomised Words Which Don't Look Even Slightly Believable. If you are going to use a Passage of Lorem Ipsum you Need to be Sure There isn't Anything Embarrassing Hidden in the Middle of Text. All the Lorem Ipsum Generators on the Internet Tend to Repeat Predefined Chunks as Necessary Making this the First True Generator on the Internet. It uses a Dictionary of Over 200 Latin Words Combined with a Handful of Model Sentence Structures to Generate Lorem Ipsum Which Looks Reasonable. The Generated Lorem Ipsum is Therefore Always Free from Repetition Injected Humour or Non-Characteristic Words etc. Contrary to Popular Belief. Lorem Ipsum is not Simply Random Text. It has roots.</p>

<ul class="abs bullets" style="left:26px">
  <li><svg viewBox="0 0 10 10"><circle cx="5" cy="5" r="5" fill="#1c2b57"/><path d="M2.5 5h4M5 3l2 2-2 2" stroke="#fff" fill="none" stroke-width="1.2"/></svg>Lorem Ipsum Dolor Sit Amet</li>
  <li><svg viewBox="0 0 10 10"><circle cx="5" cy="5" r="5" fill="#1c2b57"/><path d="M2.5 5h4M5 3l2 2-2 2" stroke="#fff" fill="none" stroke-width="1.2"/></svg>Consectetur Adipiscing Elit</li>
  <li><svg viewBox="0 0 10 10"><circle cx="5" cy="5" r="5" fill="#1c2b57"/><path d="M2.5 5h4M5 3l2 2-2 2" stroke="#fff" fill="none" stroke-width="1.2"/></svg>Aenean Nec Turpis a Enim</li>
  <li><svg viewBox="0 0 10 10"><circle cx="5" cy="5" r="5" fill="#1c2b57"/><path d="M2.5 5h4M5 3l2 2-2 2" stroke="#fff" fill="none" stroke-width="1.2"/></svg>Elementum Gravida</li>
  <li><svg viewBox="0 0 10 10"><circle cx="5" cy="5" r="5" fill="#1c2b57"/><path d="M2.5 5h4M5 3l2 2-2 2" stroke="#fff" fill="none" stroke-width="1.2"/></svg>Nam Quis Sem Tincidunt</li>
</ul>
<ul class="abs bullets" style="left:238px">
  <li><svg viewBox="0 0 10 10"><circle cx="5" cy="5" r="5" fill="#1c2b57"/><path d="M2.5 5h4M5 3l2 2-2 2" stroke="#fff" fill="none" stroke-width="1.2"/></svg>Lorem Ipsum Dolor Sit Amet</li>
  <li><svg viewBox="0 0 10 10"><circle cx="5" cy="5" r="5" fill="#1c2b57"/><path d="M2.5 5h4M5 3l2 2-2 2" stroke="#fff" fill="none" stroke-width="1.2"/></svg>Consectetur Adipiscing Elit.</li>
  <li><svg viewBox="0 0 10 10"><circle cx="5" cy="5" r="5" fill="#1c2b57"/><path d="M2.5 5h4M5 3l2 2-2 2" stroke="#fff" fill="none" stroke-width="1.2"/></svg>Aenean Nec Turpis a Enim</li>
  <li><svg viewBox="0 0 10 10"><circle cx="5" cy="5" r="5" fill="#1c2b57"/><path d="M2.5 5h4M5 3l2 2-2 2" stroke="#fff" fill="none" stroke-width="1.2"/></svg>Elementum Gravida</li>
  <li><svg viewBox="0 0 10 10"><circle cx="5" cy="5" r="5" fill="#1c2b57"/><path d="M2.5 5h4M5 3l2 2-2 2" stroke="#fff" fill="none" stroke-width="1.2"/></svg>Nam Quis Sem Tincidunt</li>
</ul>
<ul class="abs bullets" style="left:450px">
  <li><svg viewBox="0 0 10 10"><circle cx="5" cy="5" r="5" fill="#1c2b57"/><path d="M2.5 5h4M5 3l2 2-2 2" stroke="#fff" fill="none" stroke-width="1.2"/></svg>Lorem Ipsum Dolor Sit Amet</li>
  <li><svg viewBox="0 0 10 10"><circle cx="5" cy="5" r="5" fill="#1c2b57"/><path d="M2.5 5h4M5 3l2 2-2 2" stroke="#fff" fill="none" stroke-width="1.2"/></svg>Consectetur Adipiscing Elit</li>
  <li><svg viewBox="0 0 10 10"><circle cx="5" cy="5" r="5" fill="#1c2b57"/><path d="M2.5 5h4M5 3l2 2-2 2" stroke="#fff" fill="none" stroke-width="1.2"/></svg>Aenean Nec Turpis a Enim</li>
  <li><svg viewBox="0 0 10 10"><circle cx="5" cy="5" r="5" fill="#1c2b57"/><path d="M2.5 5h4M5 3l2 2-2 2" stroke="#fff" fill="none" stroke-width="1.2"/></svg>Elementum Gravida</li>
  <li><svg viewBox="0 0 10 10"><circle cx="5" cy="5" r="5" fill="#1c2b57"/><path d="M2.5 5h4M5 3l2 2-2 2" stroke="#fff" fill="none" stroke-width="1.2"/></svg>Nam Quis Sem Tincidunt</li>
</ul>

<div class="abs hero" role="img" aria-label="Photo of a domed rotunda with colonnades reflected in a lagoon under blue sky"></div>

<div class="abs issue">
  <svg class="panel-bg" viewBox="0 0 163 90" preserveAspectRatio="none"><path d="M0 0H163V72L82 90 0 72Z" fill="#1c2b57"/><path d="M0 72 82 90 163 72" stroke="#fff" stroke-width="3" fill="none"/></svg>
  ISSUE NO. 05<br>SEPT. 2016
  <svg width="24" height="8" viewBox="0 0 24 8" style="display:block;margin:3px auto 0"><path d="M0 4h24M9 1l3 3-3 3M15 1l-3 3 3 3" stroke="#fff" fill="none" stroke-width=".8"/></svg>
</div>

<header class="abs masthead">
  <h1>Cypress Report Update</h1>
  <p>The Latest Real Estate News and Listings</p>
</header>

<aside class="abs sidebar">
  <svg class="panel-bg" viewBox="0 0 163 349" preserveAspectRatio="none"><path d="M0 0H163V322L82 349 0 322Z" fill="#1c2b57"/></svg>
  <div class="portrait" role="img" aria-label="Portrait photo of the agent"></div>
  <div class="name">DANIEL HALE</div>
  <div class="role">Luxury Property Specialist</div>
  <div class="brokerage"><div class="mark">Harbor Vine</div><div class="sub">REALTY GROUP</div></div>
</aside>

<article class="abs article">
  <h2>Second Quarter in Review</h2>
  <p class="dek">Looking back on what happened in the SF housing market</p>
  <p class="body">Since 2012, San Francisco’s overall average sales price has shown tremendous growth year over year. With San Francisco leading the charge after the 2008 market recession, available inventory dwindled and sales prices climbed annually throughout the City. However, second quarter 2016 data from the San Francisco Multiple Listing Service reflected that, while the San Francisco real estate market remains vibrant and strong, there has been a shift in direction. After seeing significant year-over-year gains, the average sales price throughout San Francisco for single-family homes fell slightly, 2.8 percent, decreasing from an average of $1,79 million in the second quarter of 2015, to an average of $1.74 million in the second quarter of 2016. In our review of seven major districts in the City, we found the average sales price in the second quarter of 2016 for a single-family home decreased in five of them, compared to the second quarter of 2015. In four of the seven districts we analyzed, the average sales price year-over-year for a condominium saw a decline. Throughout the City, condominiums saw a 2.2 percent drop in average sales price, with the average sales price at $1.36 million in the second quarter of 2015, to the average of $1.29 million in the second quarter of 2016.</p>
</article>

<figure class="abs chart">
  <svg width="420" height="198" viewBox="0 0 420 198">
    <path d="M0 198C10 170 15 130 25 128C40 126 45 160 60 150C80 130 90 80 110 58C125 45 130 70 150 95C175 118 185 110 200 125C220 135 240 130 260 120C290 110 300 95 330 118C355 135 365 145 380 170C390 185 400 195 420 198Z" fill="#f7913d"/>
    <path d="M0 198C15 175 25 150 40 140C60 128 75 110 100 95C130 80 160 40 185 30C205 25 220 60 240 90C255 110 270 120 285 120C300 118 305 85 320 90C340 100 345 150 360 160C380 170 400 190 420 198Z" fill="#1c2b57" fill-opacity=".93"/>
    <path d="M0 198C30 180 50 175 70 170C100 162 130 150 160 130C190 115 210 95 230 83C250 72 262 90 275 110C290 130 300 135 320 140C345 150 355 165 375 175C395 185 410 195 420 198Z" fill="#0f6b45" fill-opacity=".95"/>
    <g stroke="#f7913d" stroke-width="1.5"><line x1="25" y1="70" x2="25" y2="128"/><circle cx="25" cy="70" r="2.5" fill="#f7913d"/></g>
    <g stroke="#1c2b57" stroke-width="1.5"><line x1="185" y1="0" x2="185" y2="30"/><circle cx="185" cy="30" r="2.5" fill="#1c2b57"/></g>
    <g stroke="#0f6b45" stroke-width="1.5"><line x1="325" y1="66" x2="325" y2="142"/><circle cx="325" cy="66" r="2.5" fill="#0f6b45"/></g>
  </svg>
  <span class="chart-label" style="left:-8px;top:54px;color:var(--orange)">Median Price</span>
  <span class="chart-label" style="left:136px;top:-6px;color:var(--navy)">Homes Sold</span>
  <span class="chart-label" style="left:264px;top:45px;color:var(--green)">Average Days on Market</span>
</figure>

</body>
</html>
```